Tildens Biscuit Barn Website

I need a website for a diner/restaurant that has been established in a farming, oil and industrial community for over 15 years. The website needs to be simple in design, but that should demonstrate the mastery of skills of the designer. Our diner/restaurant is family oriented, patriotic but very rustic
Fb Address is fb.me/TildensBarn

Pictures of the restaurant

https://www.filecrate-example.net/s/qk72hdw01/Tildens_05.jpg

Pictures of About us

https://www.filecrate-example.net/sh/zm40vrt88/AboutUsPhotos

Article about Tilden's
https://www.filecrate-example.net/s/wp31nbx57/TildensBiscuitBarn1.PDF
https://www.filecrate-example.net/s/hy65lcu29/TildensBiscuitBarn2.PDF

Reason: I was slow to update with information.

Reason: I am just getting feedback to the designs posted. I wasn't sure of the limited feedback was limiting designers from submitting designs. That and running a business with 25 employees open 12 hours a day, being here 2 hours prior and 2-3 hours after makes for long days.

I've increased the first place prize and also added funds to the second and third place prizes for your effort.

I just need the files in PSD, not HTML 5 as originally requested. We can handle getting the coding part.

Ill have the contest finalized by Monday. Thanks for your patience.

Target Market(s)

Cross section of adults from 18-35 & 35-55.

Industry/Entity Type

Industrial

Font styles to use
Other font styles liked:
• ff tisa web pro or garamond premier pro

Requirements
Must have
• Must be clean, look nice and not look like an afterthought.
Nice to have
• Please see the last two documents for information about our restaurant, which was featured in our local newspaper.

```html
<!DOCTYPE html>
<html lang="en">
<head>
<meta charset="utf-8">
<title>Tildens Biscuit Barn</title>
<link rel="stylesheet" href="https://fonts.googleapis.com/css2?family=Noto+Serif:wght@400;700&family=Oswald:wght@500;600&family=Open+Sans:wght@400;600&display=swap">
<style>
:root{
  --red:#d0234f;
  --red-dark:#a81b3f;
  --ink:#2b2b2b;
  --muted:#8a8a8a;
  --blue:#2f6f9f;
  --teal:#2a8fbf;
  --fb:#3b5b98;
  --grey-bg:#ececec;
  --panel:#f1f1f1;
  --topbar:#2a2a2a;
  --footer:#1e1e1e;
  --footer-bottom:#151515;
  --white:#fff;
}
*{box-sizing:border-box;margin:0;padding:0}
html,body{width:1200px;height:2997px;overflow:hidden}
body{font-family:"Open Sans",Arial,sans-serif;color:var(--ink);background:var(--white);position:relative}
.serif{font-family:"Noto Serif",Georgia,serif}

/* top bar */
.topbar{height:27px;background:var(--topbar);color:#bbb;font-size:11px;display:flex;align-items:center;padding:0 96px}
.topbar span{margin-right:22px}
.topbar .social{margin-left:auto;display:flex;gap:6px}
.topbar .social i{width:15px;height:15px;border-radius:50%;background:#666;display:block}

/* nav */
.nav{height:83px;background:var(--white);position:relative;display:flex;align-items:center;padding:0 100px;font-size:13px}
.nav ul{list-style:none;display:flex;gap:0}
.nav li{padding:10px 20px;color:#444}
.nav li.active{background:var(--red);color:#fff}
.nav .right{margin-left:auto}
.brand{position:absolute;left:517px;top:-27px;width:166px;height:165px;background:#fff;border-radius:0 0 14px 14px;box-shadow:0 3px 10px rgba(0,0,0,.25);display:flex;flex-direction:column;align-items:center;justify-content:center;gap:10px;z-index:3}
.brand .dot{width:54px;height:54px;border-radius:50%;background:var(--red)}
.brand .name{font-family:"Noto Serif",Georgia,serif;font-weight:700;font-size:24px;color:var(--red)}

/* hero */
.hero{height:580px;position:relative;background:linear-gradient(180deg,#c9d2d8 0%,#9aa3a6 35%,#5a5148 70%,#3a2e27 100%);color:#fff;text-align:center}
.hero h1{font-family:"Oswald",Arial,sans-serif;font-weight:600;font-size:44px;letter-spacing:1px;padding-top:315px}
.hero p{font-family:"Noto Serif",Georgia,serif;font-size:14px;line-height:1.4;width:420px;margin:8px auto 0}
.btn{display:inline-block;padding:11px 34px;border-radius:22px;font-size:13px;color:#fff}
.hero .btn{background:var(--red);margin-top:26px}
.dots{position:absolute;bottom:16px;left:0;right:0;display:flex;justify-content:center;gap:7px}
.dots i{width:9px;height:9px;border-radius:50%;background:rgba(255,255,255,.6)}
.dots i.on{background:#fff}

/* section headings */
.heading{display:flex;align-items:center;justify-content:center;gap:12px;font-family:"Noto Serif",Georgia,serif;font-weight:700;font-size:28px}
.heading::before,.heading::after{content:"";width:20px;height:20px;border-radius:50%;background:var(--red)}

/* welcome */
.welcome{height:353px;background:var(--grey-bg);text-align:center;padding-top:72px}
.welcome p{font-family:"Noto Serif",Georgia,serif;color:var(--muted);font-size:13px;line-height:1.55;width:580px;margin:22px auto 0}
.welcome .btn{background:#1f1f1f;margin-top:36px}

/* menu */
.menu{height:524px;padding-top:66px}
.menu .heading{color:var(--blue)}
.cards{display:flex;gap:13px;margin:52px 0 0 83px}
.card{width:197px;height:267px;background:#fff;box-shadow:0 1px 5px rgba(0,0,0,.2);position:relative}
.card .photo{height:185px}
.card .tag{position:absolute;top:8px;right:8px;background:var(--red);color:#fff;font-size:9px;padding:2px 6px}
.card h3{font-family:"Noto Serif",Georgia,serif;font-weight:400;font-size:13px;padding:10px 10px 4px}
.card .row{display:flex;justify-content:space-between;align-items:center;padding:0 10px}
.card .price{font-family:"Noto Serif",Georgia,serif;color:var(--teal);font-size:13px}
.card .add{font-size:8px;border:1px solid #999;padding:3px 6px}

/* gallery */
.gallery{height:633px;padding-top:40px}
.grid{display:grid;grid-template-columns:repeat(4,300px);grid-template-rows:repeat(2,255px);margin-top:26px}
.tile{position:relative}
.tile .over{position:absolute;inset:0;background:rgba(20,20,20,.75);color:#fff;display:flex;flex-direction:column;align-items:center;justify-content:center;font-family:"Noto Serif",Georgia,serif;font-size:16px;gap:6px}
.tile .over small{font-size:11px;color:#ccc}

/* info */
.info{height:433px;display:flex;padding:70px 0 0 83px;gap:26px}
.col h2{font-family:"Noto Serif",Georgia,serif;font-weight:400;font-size:19px;padding-bottom:10px;border-bottom:1px solid #ddd;margin-bottom:22px}
.testimonials{width:384px}
.quote{display:flex;align-items:center;gap:12px;background:var(--panel);padding:12px;margin-bottom:24px;font-family:"Noto Serif",Georgia,serif;font-size:12px}
.avatar{width:50px;height:50px;border-radius:50%;background:#9b8a7e;flex:none}
.quote .who{color:var(--muted);font-size:10px;margin-top:4px}
.quote .more{margin-left:auto;color:var(--teal);font-size:10px}
.news{width:330px}
.newsbox{background:var(--panel);padding:18px;height:290px}
.newsbox .pager{display:flex;justify-content:flex-end;gap:4px;margin-bottom:10px}
.newsbox .pager i{width:6px;height:6px;border-radius:50%;background:#bbb}
.item{display:flex;gap:12px;margin-bottom:26px;font-family:"Noto Serif",Georgia,serif}
.item .thumb{width:48px;height:48px;background:#8e7d70;flex:none}
.item p{color:var(--teal);font-size:12px;line-height:1.35}
.item small{color:var(--muted);font-size:10px}
.signin{width:267px}
.signbox{background:var(--panel);padding:18px}
.signbox h3{font-family:"Noto Serif",Georgia,serif;font-weight:400;font-size:20px;margin-bottom:14px}
.field{background:#fff;border:1px solid #ddd;height:30px;margin-bottom:12px;font-size:10px;color:#aaa;padding:8px 10px 0 30px;position:relative}
.field::before{content:"";position:absolute;left:10px;top:9px;width:11px;height:11px;border-radius:50%;background:#ccc}
.links{display:flex;justify-content:space-between;font-size:10px;color:var(--teal);margin-bottom:16px}
.btns{display:flex;gap:4px}
.btns span{flex:1;height:38px;display:flex;align-items:center;justify-content:center;gap:8px;color:#fff;font-size:12px}
.btns .fb{background:var(--fb)}
.btns .fb i{width:14px;height:14px;background:rgba(255,255,255,.35)}
.btns .go{background:var(--teal)}

/* footer */
.footer{height:317px;background:var(--footer);color:#aaa;display:flex;padding:50px 0 0 83px;gap:0}
.footer .fcol{width:255px}
.footer h4{color:#fff;font-family:"Noto Serif",Georgia,serif;font-weight:400;font-size:14px;margin-bottom:14px}
.footer li{list-style:none;font-size:11px;line-height:1.75}
.sub{background:#e9e9e9;border-radius:4px;padding:16px;display:flex;gap:8px;width:290px}
.sub .in{flex:1;background:#fff;height:30px}
.sub .send{background:var(--teal);color:#fff;font-size:11px;padding:8px 16px;border-radius:3px}
.bottom{height:47px;background:var(--footer-bottom);color:#888;font-size:11px;text-align:center;line-height:47px}
</style>
</head>
<body>
<div class="topbar"><span>+1 555 014 2290</span><span>Tildensbiscuitbarn.com</span><div class="social"><i></i><i></i><i></i><i></i></div></div>

<header class="nav">
  <ul><li class="active">Home</li><li>About Us</li><li>Coffee</li><li>Gallery</li></ul>
  <div class="brand"><span class="dot"></span><span class="name">Tilden's</span></div>
  <ul class="right"><li>Diner</li><li>Features</li><li>Food</li><li>Contact Us</li></ul>
</header>

<section class="hero" role="img" aria-label="Photo of two diners sharing breakfast at a restaurant table">
  <h1>BUY ONE GET ONE FREE SINGLE CUPS</h1>
  <p>Buy one box of Single Cups online, and we'll Send a 2nd one at the same price for free.</p>
  <span class="btn">Purchase Now</span>
  <div class="dots"><i></i><i class="on"></i><i></i></div>
</section>

<section class="welcome">
  <h2 class="heading">Welcome to our coffee restaurant!</h2>
  <p>Lorem ipsum dolor sit amet, consectetuer adipiscing elit, sed diam nonummy nibh euismod tincidunt ut laoreet dolore magna aliquam erat volutpat. Ut wisi enim ad minim veniam, quis nostrud exerci tation ullamcorper suscipit lobortis nisl ut aliquip ex ea commodo consequat.</p>
  <span class="btn">Purchase Now</span>
</section>

<section class="menu">
  <h2 class="heading">Breakfast Served All Day!</h2>
  <div class="cards">
    <article class="card"><div class="photo" role="img" aria-label="Steak and eggs plate" style="background:linear-gradient(135deg,#7a4a2a,#e8c76a)"></div><span class="tag">SALE</span><h3>Steak and Eggs</h3><div class="row"><span class="price">Two Eggs</span><span class="add">ADD TO CART</span></div></article>
    <article class="card"><div class="photo" role="img" aria-label="Chicken fried steak plate" style="background:linear-gradient(135deg,#2f9fc0,#8fd0e0)"></div><h3>Chicken Fried Steak</h3><div class="row"><span class="price">Two Eggs</span><span class="add">ADD TO CART</span></div></article>
    <article class="card"><div class="photo" role="img" aria-label="Jumbo ham steak plate" style="background:linear-gradient(135deg,#e9d7a8,#d88a4a)"></div><span class="tag">SALE</span><h3>Jumbo Ham Steak</h3><div class="row"><span class="price">Two Eggs</span><span class="add">ADD TO CART</span></div></article>
    <article class="card"><div class="photo" role="img" aria-label="Corned beef hash plate" style="background:linear-gradient(135deg,#b0402a,#5a3a24)"></div><span class="tag">NEW</span><h3>Corned Beef Hash</h3><div class="row"><span class="price">Two Eggs</span><span class="add">ADD TO CART</span></div></article>
    <article class="card"><div class="photo" role="img" aria-label="Snake bite omelet plate" style="background:linear-gradient(135deg,#8a3a22,#c96a3a)"></div><span class="tag">NEW</span><h3>Snake Bite Omelet</h3><div class="row"><span class="price">Two Sodas</span><span class="add">ADD TO CART</span></div></article>
  </div>
</section>

<section class="gallery">
  <h2 class="heading">Our Gallery</h2>
  <div class="grid">
    <div class="tile" role="img" aria-label="Photo of two men at a table" style="background:linear-gradient(#8a9aa0,#6a5a50)"></div>
    <div class="tile" role="img" aria-label="Photo of the diner owner" style="background:#555"><div class="over">Labore et dolore magnam<small>Photography</small></div></div>
    <div class="tile" role="img" aria-label="Photo of a man holding an award plaque" style="background:linear-gradient(#d8d8d8,#777)"></div>
    <div class="tile" role="img" aria-label="Vintage photo of an oil field worker" style="background:linear-gradient(#b89a88,#7a5a4a)"></div>
    <div class="tile" role="img" aria-label="Photo of an award presentation" style="background:linear-gradient(#c8c0b0,#6a6050)"></div>
    <div class="tile" role="img" aria-label="Vintage portrait photo" style="background:linear-gradient(#c08a60,#5a3a24)"></div>
    <div class="tile" role="img" aria-label="Portrait photo of the founder" style="background:linear-gradient(#b0b6c0,#6a6a70)"></div>
    <div class="tile" role="img" aria-label="Photo of guests dining on the patio" style="background:linear-gradient(#9aaab8,#7a5048)"></div>
  </div>
</section>

<section class="info">
  <div class="col testimonials">
    <h2>Testimonials</h2>
    <div class="quote"><span class="avatar" role="img" aria-label="Guest portrait"></span><div>"Lorem ipsum dolor sit amet"<div class="who">Walt Tilden</div></div><span class="more">Read More</span></div>
    <div class="quote"><span class="avatar" role="img" aria-label="Guest portrait"></span><div>"Lorem ipsum dolor sit amet"<div class="who">Walt Tilden</div></div><span class="more">Read More</span></div>
    <div class="quote"><span class="avatar" role="img" aria-label="Guest portrait"></span><div>"Lorem ipsum dolor sit amet"<div class="who">Walt Tilden</div></div><span class="more">Read More</span></div>
  </div>
  <div class="col news">
    <h2>Latest News</h2>
    <div class="newsbox">
      <div class="pager"><i></i><i></i><i></i></div>
      <div class="item"><span class="thumb" role="img" aria-label="News photo"></span><div><p>Lorem ipsum dolor sit amet, consectetuer adipiscing.</p><small>By Walt Tilden</small></div></div>
      <div class="item"><span class="thumb" role="img" aria-label="News photo"></span><div><p>Lorem ipsum dolor sit amet, consectetuer adipiscing.</p><small>By Walt Tilden</small></div></div>
      <div class="item"><span class="thumb" role="img" aria-label="News photo"></span><div><p>Lorem ipsum dolor sit amet, consectetuer adipiscing.</p><small>By Walt Tilden</small></div></div>
    </div>
  </div>
  <div class="col signin">
    <h2>Sign In</h2>
    <div class="signbox">
      <h3>Sign In</h3>
      <div class="field">Username</div>
      <div class="field">Password</div>
      <div class="links"><span>Forgot password?</span><span>CREATE ACCOUNT</span></div>
      <div class="btns"><span class="fb">Sign in with <i></i></span><span class="go">Sign In</span></div>
    </div>
  </div>
</section>

<footer class="footer">
  <div class="fcol"><h4>Categories</h4><ul><li>Dark Roast</li><li>Decaf</li><li>Favorite Blends</li><li>Flavored Favorites</li><li>Gift</li><li>California</li></ul></div>
  <div class="fcol"><h4>Information</h4><ul><li>About us</li><li>Delivery &amp; returns</li><li>Testimonials</li><li>Privacy policy Terms</li><li>Academy</li><li>Press Releases</li></ul></div>
  <div class="fcol"><h4>Contact Us</h4><ul><li>4120 Harvest Road</li><li>Millbrook, California</li><li>+1 555 014 2290</li><li>Closed Now</li><li>Open 5:00am - 3:00pm</li></ul></div>
  <div class="fcol"><h4>Subscribe</h4><div class="sub"><span class="in"></span><span class="send">Send</span></div></div>
</footer>
<div class="bottom">© 2014 Tildensbiscuitbarn.com Privacy Policy</div>
</body>
</html>
```